Business Card design for an International Import Export House

We need a Business Card design for our import export business. We trade in Minerals, Metals, Rice, Sugar, Steel etc.. The design should be minimalistic. It may or may not contain the physical address. In case you want to include the physical address - 418 Verandah Heights, Marlow Sector 9, Kestrel Nagar, Ambara, India, 560418.

Target Market(s)

Steel Mills or Steel Plants, Factories, Mining businesses, Industrial houses, Government Agencies

Industry/Entity Type

Importer

Contact Information for Business Card

Business Name - Halvern Overseas

Font styles to use
Other font styles liked:
• montserrat

Requirements
Must have
• Ravi Kandola - President
• www.halvernoverseas.com
• ravi@halvernoverseas.com
• +91-987-654-3217
Nice to have
• worldwide suppliers of ores

```html
<!DOCTYPE html>
<html lang="en">
<head>
<meta charset="utf-8">
<title>Halvern Overseas — Business Card</title>
<link rel="stylesheet" href="https://fonts.googleapis.com/css2?family=Montserrat:wght@300;400;500;700&display=swap">
<style>
  :root {
    --canvas: #ecebe8;
    --card: #ffffff;
    --teal: #3a8fa8;
    --teal-light: #5fb3c8;
    --ink: #1f2326;
    --ink-soft: #3a3f44;
    --rule: #8fc3d2;
  }
  * { box-sizing: border-box; margin: 0; padding: 0; }
  html, body {
    width: 1200px; height: 1200px; overflow: hidden;
    background: var(--canvas);
    font-family: "Montserrat", Arial, sans-serif;
    color: var(--ink);
  }
  .sheet {
    width: 1200px; height: 1200px;
    display: flex; flex-direction: column; align-items: center; justify-content: center;
    gap: 44px;
  }
  .card {
    position: relative;
    width: 900px; height: 514px;
    background: var(--card);
    box-shadow: 0 10px 30px rgba(0,0,0,0.12);
    overflow: hidden;
  }

  /* Front */
  .brand-block {
    position: absolute; left: 0; top: 0; width: 450px; height: 424px;
    display: flex; align-items: center; justify-content: center; gap: 16px;
  }
  .brand-dot {
    width: 30px; height: 30px; border-radius: 50%; background: var(--teal); flex: none;
  }
  .brand-name {
    font-weight: 700; font-size: 30px; letter-spacing: -0.5px;
    color: var(--teal); text-transform: uppercase; white-space: nowrap;
  }
  .divider {
    position: absolute; left: 450px; top: 40px; width: 1.5px; height: 384px;
    background: linear-gradient(to bottom, rgba(143,195,210,0), var(--rule) 60%, var(--teal));
  }
  .contact-block {
    position: absolute; right: 56px; top: 64px;
    text-align: right;
  }
  .person-name { font-weight: 400; font-size: 34px; color: var(--ink); line-height: 1.1; }
  .person-role { font-weight: 500; font-size: 17px; color: var(--teal); margin-top: 4px; }
  .contact-list { list-style: none; margin-top: 78px; }
  .contact-item {
    display: flex; justify-content: flex-end; align-items: center; gap: 14px;
    font-size: 19px; font-weight: 400; color: var(--ink-soft); line-height: 1.55;
  }
  .contact-icon { width: 18px; height: 18px; flex: none; }
  .address-band {
    position: absolute; left: 0; bottom: 0; width: 100%; height: 90px;
    background: var(--teal);
    display: flex; align-items: center; padding-left: 56px;
    color: #fff; font-size: 18px; font-weight: 400; letter-spacing: 0.2px;
    white-space: nowrap;
  }

  /* Back */
  .card-back .brand-block {
    width: 100%; height: 100%; gap: 22px;
  }
  .card-back .brand-dot { width: 44px; height: 44px; background: var(--teal-light); }
  .card-back .brand-name { font-size: 40px; color: var(--ink); }
</style>
</head>
<body>
<main class="sheet">
  <section class="card card-front" aria-label="Business card front">
    <div class="brand-block">
      <span class="brand-dot"></span>
      <span class="brand-name">Halvern Overseas</span>
    </div>
    <div class="divider"></div>
    <div class="contact-block">
      <p class="person-name">Ravi Kandola</p>
      <p class="person-role">President</p>
      <ul class="contact-list">
        <li class="contact-item">+91-987-654-3217
          <svg class="contact-icon" viewBox="0 0 18 18" aria-hidden="true">
            <rect width="18" height="18" rx="2" fill="var(--teal)"/>
            <path d="M5 4.5c.6-.6 1.3-.5 1.6.1l.9 1.7c.2.4.1.8-.2 1.1l-.6.5c.5 1.1 1.4 2 2.5 2.5l.5-.6c.3-.3.7-.4 1.1-.2l1.7.9c.6.3.7 1 .1 1.6l-.7.7c-.6.6-1.6.7-2.4.3C7.6 12 6 10.4 5 8.5c-.4-.8-.3-1.8.3-2.4z" fill="#fff"/>
          </svg>
        </li>
        <li class="contact-item">www.halvernoverseas.com
          <svg class="contact-icon" viewBox="0 0 18 18" aria-hidden="true">
            <rect width="18" height="18" rx="2" fill="var(--teal)"/>
            <circle cx="9" cy="9" r="5" fill="none" stroke="#fff" stroke-width="1.2"/>
            <ellipse cx="9" cy="9" rx="2.2" ry="5" fill="none" stroke="#fff" stroke-width="1"/>
            <line x1="4" y1="9" x2="14" y2="9" stroke="#fff" stroke-width="1"/>
          </svg>
        </li>
        <li class="contact-item">ravi@halvernoverseas.com
          <svg class="contact-icon" viewBox="0 0 18 18" aria-hidden="true">
            <rect width="18" height="18" rx="2" fill="var(--teal)"/>
            <rect x="4" y="5.5" width="10" height="7" fill="none" stroke="#fff" stroke-width="1.2"/>
            <polyline points="4,5.5 9,9.5 14,5.5" fill="none" stroke="#fff" stroke-width="1.2"/>
          </svg>
        </li>
      </ul>
    </div>
    <div class="address-band">418 Verandah Heights, Marlow Sector 9, Kestrel Nagar, Ambara, India, 560418.</div>
  </section>

  <section class="card card-back" aria-label="Business card back">
    <div class="brand-block">
      <span class="brand-dot"></span>
      <span class="brand-name">Halvern Overseas</span>
    </div>
  </section>
</main>
</body>
</html>
```